Business card design needed for Pollen Bakes

We need a new business card designed for our business. We create complete DIY cake kits to be delivered Australia Wide.

I would like our logo used (see attached).

Industry/Entity Type

Business

Contact Information for Business Card

Pollen Bakes - Complete DIY Cake Kits
www.pollenbakes.com.au
0472 315 904
sales@pollenbakes.com.au
www.facebook.com/pollenbakes1

Requirements
Must have
• logo

```html
<!DOCTYPE html>
<html lang="en">
<head>
<meta charset="utf-8">
<title>Pollen Bakes – Business Card</title>
<link rel="stylesheet" href="https://fonts.googleapis.com/css2?family=Archivo+Black&family=Open+Sans:wght@700&display=swap">
<style>
  :root {
    --mint: #8fd3cd;
    --teal: #5fb3a8;
    --teal-dark: #3f8f86;
    --red: #b81c22;
    --white: #ffffff;
    --grey-icon: #b9c1c0;
    --social: #2c4f8f;
    --stage: #e4e4e2;
    --heading: "Archivo Black", "Arial Black", sans-serif;
    --body: "Open Sans", Arial, sans-serif;
  }
  * { box-sizing: border-box; margin: 0; padding: 0; }
  html, body { width: 1200px; height: 1200px; overflow: hidden; }
  body { background: var(--stage); position: relative; }

  .card {
    position: absolute;
    left: 160px;
    width: 880px;
    height: 500px;
    overflow: hidden;
    box-shadow: 0 6px 18px rgba(0,0,0,.18);
  }
  .card--back { top: 70px; }
  .card--front { top: 630px; }

  /* back side */
  .back__pattern {
    position: absolute; left: 0; top: 0; width: 510px; height: 100%;
    background: var(--mint);
  }
  .back__band {
    position: absolute; left: 510px; top: 0; width: 44px; height: 100%;
    background: var(--teal);
  }
  .back__panel {
    position: absolute; left: 554px; top: 0; right: 0; height: 100%;
    background: var(--red);
  }

  .logo {
    position: absolute;
    display: flex; flex-direction: column; align-items: center; justify-content: center;
    width: 230px; height: 230px; border-radius: 50%;
    background: var(--white);
  }
  .logo__name {
    font-family: var(--heading);
    color: var(--red);
    font-size: 30px;
    line-height: 1.1;
    text-align: center;
  }
  .logo__tag {
    font-family: var(--body);
    color: var(--teal);
    font-size: 14px;
    margin-top: 8px;
  }
  .back__logo { left: 150px; top: 30px; }
  .front__logo { left: 325px; top: 60px; width: 240px; height: 240px; }

  .contact {
    position: absolute; left: 48px;
    display: flex; align-items: center; gap: 18px;
    font-family: var(--body); color: var(--red);
    white-space: nowrap;
  }
  .contact--phone { top: 292px; font-size: 40px; letter-spacing: 2px; }
  .contact--email { top: 362px; font-size: 19px; }
  .icon {
    flex: none; width: 40px; height: 40px; border-radius: 50%;
    display: flex; align-items: center; justify-content: center;
  }
  .icon--phone { background: var(--teal-dark); }
  .icon--mail { background: var(--grey-icon); }

  .headline {
    position: absolute; left: 584px; top: 72px;
    font-family: var(--heading); font-weight: 400; line-height: 1.08; text-transform: uppercase;
    white-space: nowrap;
  }
  .headline span { display: block; }
  .headline__name { color: var(--white); font-size: 22px; letter-spacing: 2px; }
  .headline__lead { color: var(--mint); font-size: 25px; }
  .headline__kits { color: var(--white); font-size: 35px; letter-spacing: 1px; }

  .links {
    position: absolute; left: 584px; top: 236px;
    list-style: none; font-family: var(--body); color: var(--white); font-size: 13px;
    white-space: nowrap;
  }
  .links li { display: flex; align-items: center; gap: 12px; margin-bottom: 14px; }
  .links .icon { width: 28px; height: 28px; }
  .icon--social { background: var(--social); }
  .icon--web { background: var(--teal); }

  /* front side */
  .front__pattern {
    position: absolute; left: 0; top: 0; width: 100%; height: 310px;
    background: var(--mint);
  }
  .front__band {
    position: absolute; left: 0; top: 310px; width: 100%; height: 34px;
    background: var(--teal);
  }
  .front__panel {
    position: absolute; left: 0; top: 344px; width: 100%; bottom: 0;
    background: var(--red);
  }
</style>
</head>
<body>

<section class="card card--back" aria-label="Business card, back">
  <div class="back__pattern" role="img" aria-label="Mint background with white polka dot pattern"></div>
  <div class="back__band"></div>
  <div class="back__panel"></div>

  <div class="logo back__logo">
    <span class="logo__name">Pollen<br>Bakes</span>
    <span class="logo__tag">complete DIY cake kits</span>
  </div>

  <p class="contact contact--phone">
    <span class="icon icon--phone">
      <svg width="22" height="22" viewBox="0 0 24 24" aria-hidden="true"><path fill="#fff" d="M6.6 10.8a15.1 15.1 0 0 0 6.6 6.6l2.2-2.2c.3-.3.7-.4 1-.2 1.1.4 2.3.6 3.6.6.6 0 1 .4 1 1V20c0 .6-.4 1-1 1A17 17 0 0 1 3 4c0-.6.4-1 1-1h3.5c.6 0 1 .4 1 1 0 1.3.2 2.5.6 3.6.1.3 0 .7-.2 1z"/></svg>
    </span>
    0472 315 904
  </p>
  <p class="contact contact--email">
    <span class="icon icon--mail">
      <svg width="20" height="20" viewBox="0 0 24 24" aria-hidden="true"><rect x="3" y="6" width="18" height="12" rx="1.5" fill="none" stroke="#fff" stroke-width="2"/><path d="M3 7l9 6 9-6" fill="none" stroke="#fff" stroke-width="2"/></svg>
    </span>
    sales@pollenbakes.com.au
  </p>

  <h1 class="headline">
    <span class="headline__name">Pollen Bakes</span>
    <span class="headline__lead">Complete DIY</span>
    <span class="headline__kits">Cake Kits</span>
  </h1>

  <ul class="links">
    <li><span class="icon icon--social"></span>www.facebook.com/pollenbakes1</li>
    <li>
      <span class="icon icon--web">
        <svg width="16" height="16" viewBox="0 0 24 24" aria-hidden="true"><circle cx="12" cy="12" r="9" fill="none" stroke="#fff" stroke-width="2"/><path d="M3 12h18M12 3c3 3 3 15 0 18M12 3c-3 3-3 15 0 18" fill="none" stroke="#fff" stroke-width="1.6"/></svg>
      </span>
      www.pollenbakes.com.au
    </li>
  </ul>
</section>

<section class="card card--front" aria-label="Business card, front">
  <div class="front__pattern" role="img" aria-label="Mint background with white polka dot pattern"></div>
  <div class="front__band"></div>
  <div class="front__panel"></div>

  <div class="logo front__logo">
    <span class="logo__name">Pollen<br>Bakes</span>
    <span class="logo__tag">complete DIY cake kits</span>
  </div>
</section>

</body>
</html>
```